Flyer for the Lumen 2025 Conference

I am looking to produce a flyer for our upcoming conference, Lumen 2025. This is an annual conference that we plan to publicize on social media. The ideal designer will create a flyer that is eye-catching and effectively communicates the key information. Please see attached our logo, speaker photo, and flyer content.

Target Market(s)

All demographics

Industry/Entity Type

Christian

Font styles to use
Sans Serif

Requirements
Should not have
• Cross, church

```html
<!DOCTYPE html>
<html lang="en">
<head>
<meta charset="utf-8">
<title>Lumen 2025 Conference</title>
<link href="https://fonts.googleapis.com/css2?family=Anton&family=Oswald:wght@300&family=Roboto+Condensed:wght@300;400;700&family=Saira:wght@300;400&display=swap" rel="stylesheet">
<style>
  :root {
    --stage: #cfcfcf;
    --navy-deep: #0b1322;
    --navy: #1a2a44;
    --sky: #3a4f6e;
    --cream: #eddcb3;
    --gold: #b8893f;
    --gold-light: #d9b36a;
    --white: #ffffff;
    --suit: #1f5fae;
    --live-a: #5a5fd6;
    --live-b: #3b46b8;
    --red: #e3262b;
  }
  * { margin: 0; padding: 0; box-sizing: border-box; }
  html, body { width: 1043px; height: 1200px; overflow: hidden; background: var(--stage); }
  .flyer {
    position: absolute; left: 0; top: 78px; width: 1043px; height: 1043px; overflow: hidden;
    background:
      radial-gradient(ellipse 420px 300px at 330px 330px, rgba(120,140,170,.35), transparent 70%),
      radial-gradient(ellipse 500px 260px at 850px 520px, rgba(110,130,160,.35), transparent 70%),
      radial-gradient(ellipse 600px 300px at 300px 900px, rgba(70,90,120,.25), transparent 70%),
      linear-gradient(180deg, var(--navy) 0%, var(--navy-deep) 100%);
    font-family: "Roboto Condensed", sans-serif; color: var(--white);
  }
  .speaker-photo {
    position: absolute; left: 463px; top: 210px; width: 580px; height: 833px;
    background: radial-gradient(ellipse 260px 420px at 330px 470px, var(--suit) 0%, rgba(31,95,174,.55) 55%, transparent 80%);
  }
  .heading { font-weight: 400; font-size: inherit; }
  .headline-top { position: absolute; left: 53px; top: 50px; width: 444px; font-family: "Oswald", sans-serif; font-weight: 300; font-size: 86px; line-height: 1; text-align: center; white-space: nowrap; }
  .headline-sub { position: absolute; left: 53px; top: 128px; width: 444px; font-family: "Oswald", sans-serif; font-weight: 300; font-size: 44px; line-height: 1; letter-spacing: 24px; text-indent: 24px; text-align: center; white-space: nowrap; }
  .title {
    position: absolute; left: 40px; width: 490px; text-align: center; font-family: "Anton", sans-serif; line-height: 1; white-space: nowrap;
    color: var(--cream); -webkit-text-stroke: 4px var(--gold); paint-order: stroke fill;
    text-shadow: 0 4px 10px rgba(0,0,0,.6);
  }
  .title-word { top: 178px; font-size: 196px; letter-spacing: 2px; }
  .title-year { top: 372px; font-size: 196px; letter-spacing: 2px; }
  .days { position: absolute; left: 32px; top: 610px; width: 486px; display: flex; }
  .day { width: 162px; text-align: center; position: relative; }
  .day + .day::before { content: ""; position: absolute; left: 0; top: 4px; width: 2px; height: 120px; background: linear-gradient(180deg, transparent, rgba(255,255,255,.7), transparent); }
  .day-name { font-family: "Saira", sans-serif; font-weight: 300; font-size: 18px; letter-spacing: 4px; line-height: 1; }
  .day-num { font-family: "Saira", sans-serif; font-weight: 300; font-size: 80px; line-height: 72px; letter-spacing: 2px; }
  .day-month { font-family: "Saira", sans-serif; font-weight: 300; font-size: 14px; line-height: 1; margin-top: 2px; }
  .day-time { display: inline-block; margin-top: 8px; padding: 1px 6px; font-size: 15px; font-weight: 300; line-height: 16px; border-radius: 2px; background: linear-gradient(90deg, var(--gold), var(--sky) 60%, var(--gold-light)); box-shadow: 0 2px 4px rgba(0,0,0,.5); }
  .venue { position: absolute; left: 40px; top: 765px; width: 470px; text-align: center; font-weight: 300; font-size: 19px; line-height: 23px; }
  .more-label { position: absolute; left: 40px; top: 830px; width: 470px; text-align: center; font-size: 12px; letter-spacing: 3px; text-decoration: underline; font-weight: 300; }
  .more-text { position: absolute; left: 40px; top: 848px; width: 470px; text-align: center; font-size: 19px; font-weight: 300; }
  .store { position: absolute; top: 877px; height: 40px; border: 1.5px solid var(--white); border-radius: 6px; background: #000; display: flex; align-items: center; gap: 8px; padding-left: 12px; font-size: 19px; font-weight: 400; }
  .store-dot { width: 16px; height: 16px; background: var(--white); }
  .store-play { left: 127px; width: 142px; }
  .store-market { left: 281px; width: 142px; }
  .contact { position: absolute; left: 109px; top: 935px; font-weight: 700; font-size: 17px; line-height: 28px; list-style: none; }
  .contact-line { display: flex; align-items: center; gap: 8px; }
  .contact-line svg { width: 17px; height: 17px; flex: none; }
  .live { position: absolute; left: 310px; top: 956px; width: 131px; height: 35px; border-radius: 18px; background: linear-gradient(90deg, var(--live-a), var(--live-b)); display: flex; align-items: center; justify-content: center; gap: 8px; }
  .live-text { text-align: center; font-weight: 700; line-height: 12px; }
  .live-text .big { font-size: 14px; letter-spacing: 2px; display: block; }
  .live-text .small { font-size: 11px; display: block; }
  .live-dot { width: 20px; height: 20px; border-radius: 50%; background: var(--red); }
  .brand { position: absolute; left: 700px; top: 88px; width: 272px; display: flex; align-items: center; gap: 10px; font-family: "Roboto Condensed", sans-serif; font-weight: 400; font-size: 66px; line-height: 1; color: var(--white); }
  .brand-mark { width: 26px; height: 26px; border-radius: 50%; background: #f08a1c; flex: none; }
  .speaker { position: absolute; left: 859px; top: 314px; }
  .speaker-label { font-weight: 700; font-size: 21px; letter-spacing: 3px; }
  .speaker-name { font-weight: 700; font-size: 44px; line-height: 39px; margin-top: 4px; text-shadow: 0 2px 6px rgba(0,0,0,.5); }
</style>
</head>
<body>
<main class="flyer">
  <div class="speaker-photo" role="img" aria-label="Portrait of the speaker in a bright blue suit and grey knit sweater, seated"></div>

  <h1 class="heading">
    <span class="headline-top">A PROPHETIC</span>
    <span class="headline-sub">CONFERENCE</span>
    <span class="title title-word">LUMEN</span>
    <span class="title title-year">2025</span>
  </h1>

  <section class="days">
    <div class="day">
      <div class="day-name">FRIDAY</div>
      <div class="day-num">26</div>
      <div class="day-month">December 2025</div>
      <div class="day-time">6:30PM - 9:00PM</div>
    </div>
    <div class="day">
      <div class="day-name">SATURDAY</div>
      <div class="day-num">27</div>
      <div class="day-month">December 2025</div>
      <div class="day-time">5:30PM - 8:00PM</div>
    </div>
    <div class="day">
      <div class="day-name">SUNDAY</div>
      <div class="day-num">29</div>
      <div class="day-month">December 2025</div>
      <div class="day-time">4:30PM - 7:00PM</div>
    </div>
  </section>

  <p class="venue">The Harborview Performing Arts Center<br>250 Linden Avenue Fairhaven, Maine 04010</p>

  <p class="more-label">MORE INFO</p>
  <p class="more-text">Download the VESPER App to stay updated on the event</p>

  <div class="store store-play"><span class="store-dot"></span>Play Shelf</div>
  <div class="store store-market"><span class="store-dot"></span>App Market</div>

  <ul class="contact">
    <li class="contact-line">
      <svg viewBox="0 0 24 24" fill="#fff"><path d="M6.6 10.8a15.1 15.1 0 0 0 6.6 6.6l2.2-2.2a1 1 0 0 1 1-.25 11.4 11.4 0 0 0 3.6.57 1 1 0 0 1 1 1V20a1 1 0 0 1-1 1A17 17 0 0 1 3 4a1 1 0 0 1 1-1h3.5a1 1 0 0 1 1 1c0 1.250.2 2.450.57 3.57a1 1 0 0 1-.25 1z"/></svg>
      207 555 0148
    </li>
    <li class="contact-line">
      <svg viewBox="0 0 24 24" fill="none" stroke="#fff" stroke-width="2"><rect x="3" y="5" width="18" height="14" rx="2"/><path d="M3 7l9 6 9-6"/></svg>
      contact@vesper.org
    </li>
    <li class="contact-line">
      <svg viewBox="0 0 24 24" fill="none" stroke="#fff" stroke-width="2"><circle cx="12" cy="12" r="9"/><path d="M3 12h18M12 3c3 3 3 15 0 18M12 3c-3 3-3 15 0 18"/></svg>
      www.vesper.org
    </li>
  </ul>

  <div class="live">
    <div class="live-text"><span class="big">LIVE</span><span class="small">STREAMING</span></div>
    <span class="live-dot"></span>
  </div>

  <div class="brand"><span class="brand-mark"></span>VESPER</div>

  <div class="speaker">
    <div class="speaker-label">SPEAKER</div>
    <div class="speaker-name">PROPHET<br>SAMUEL<br>ARDEN</div>
  </div>
</main>
</body>
</html>
```